Flyer Design

We are a property company and need attractive flyers that will grab peoples attention. We want them to be bold but simple and not too busy. I attach a draft and also our logo. We will print in A5 size.
Thank you & I look forward to receiving designs.

It Company

```html
<!DOCTYPE html>
<html lang="en">
<head>
<meta charset="utf-8">
<title>Kaweka Subdivisions Flyer</title>
<link href="https://fonts.googleapis.com/css2?family=Open+Sans:ital,wght@0,300;0,400;0,700;1,700&display=swap" rel="stylesheet">
<style>
  :root {
    --stage: #e4e5e7;
    --paper: #ffffff;
    --ink: #2e2e2e;
    --brand-red: #b3262f;
    --brand-blue: #1638d8;
    --photo-top: #5a86cf;
    --photo-bottom: #5f8f3e;
    --wood-light: #ece3d0;
    --wood-dark: #d8ccb3;
    --brand-ink: #6a5a35;
  }
  html, body {
    margin: 0;
    width: 1200px;
    height: 1000px;
    overflow: hidden;
    background: var(--stage);
    font-family: "Open Sans", Arial, sans-serif;
  }
  .flyer {
    position: absolute;
    left: 280px;
    top: 50px;
    width: 640px;
    height: 900px;
    background: var(--paper);
    box-shadow: 0 6px 18px rgba(0,0,0,0.25);
    overflow: hidden;
  }
  .hero-photo {
    position: absolute;
    inset: 0 0 auto 0;
    height: 420px;
    background: linear-gradient(180deg, var(--photo-top) 0%, var(--photo-bottom) 100%);
  }
  .headline {
    position: absolute;
    margin: 0;
    display: flex;
    align-items: center;
    gap: 10px;
    color: #fff;
    font-weight: 700;
    line-height: 1.1;
    text-shadow: 0 1px 3px rgba(0,0,0,0.35);
  }
  .headline svg { flex: none; }
  .headline--freedom { left: 62px; top: 58px; font-size: 30px; }
  .headline--subdivisions { left: 290px; top: 240px; font-size: 25px; }
  .body-copy {
    position: absolute;
    left: 62px;
    right: 50px;
    top: 448px;
    color: var(--ink);
    font-weight: 300;
    font-size: 19px;
    line-height: 1.32;
  }
  .body-copy p { margin: 0 0 20px; }
  .body-copy strong { font-weight: 700; color: #111; }
  .web-address {
    position: absolute;
    right: 40px;
    top: 738px;
    color: var(--brand-red);
    font-weight: 700;
    font-style: italic;
    font-size: 22px;
  }
  .footer {
    position: absolute;
    left: 0; right: 0; bottom: 0;
    height: 108px;
    display: flex;
  }
  .call-band {
    flex: 0 0 62%;
    background: var(--brand-red);
    color: #fff;
    display: flex;
    align-items: center;
    justify-content: center;
    gap: 8px;
    font-size: 36px;
    font-weight: 300;
  }
  .call-band b { font-weight: 700; }
  .brand-panel {
    flex: 1;
    background: linear-gradient(135deg, var(--wood-light), var(--wood-dark));
    display: flex;
    align-items: center;
    justify-content: center;
    color: var(--brand-ink);
    font-family: "Open Sans", Arial, sans-serif;
    font-weight: 400;
    font-size: 19px;
  }
</style>
</head>
<body>
  <main class="flyer">
    <div class="hero-photo" role="img" aria-label="Photo of a surveyor with a survey instrument in front of a modern house on a lawn under a blue sky"></div>

    <h1 class="headline headline--freedom">
      <svg width="62" height="74" viewBox="0 0 62 74" aria-hidden="true">
        <rect x="1" y="8" width="60" height="58" fill="var(--brand-blue)" stroke="#fff" stroke-width="2"/>
        <line x1="31" y1="0" x2="31" y2="74" stroke="#fff" stroke-width="2"/>
      </svg>
      <span>Looking for<br>financial freedom?</span>
    </h1>

    <h2 class="headline headline--subdivisions">
      <svg width="62" height="74" viewBox="0 0 62 74" aria-hidden="true">
        <rect x="1" y="8" width="60" height="58" fill="var(--brand-blue)" stroke="#fff" stroke-width="2"/>
        <line x1="31" y1="0" x2="31" y2="74" stroke="#fff" stroke-width="2"/>
      </svg>
      <span>We specialise in<br>subdivisions</span>
    </h2>

    <section class="body-copy">
      <p>Are you a homeowner looking for financial freedom while been able to keep your own home?</p>
      <p>Are you struggling to pay your mortgage?</p>
      <p>Kaweka specialise in subdivisions including finance and management.</p>
      <p>Email <strong>info@kawekasubdivisions.com</strong> for more information or to find out if your property is suitable for subdivision in Auckland.</p>
    </section>

    <div class="web-address">www.kawekasubdivisions.com</div>

    <footer class="footer">
      <div class="call-band">
        <svg width="22" height="36" viewBox="0 0 22 36" aria-hidden="true">
          <rect x="2" y="2" width="18" height="32" rx="3" fill="none" stroke="#fff" stroke-width="3"/>
          <line x1="8" y1="29" x2="14" y2="29" stroke="#fff" stroke-width="2"/>
        </svg>
        <span><b>Call</b> 021 555 0147</span>
      </div>
      <div class="brand-panel">Kaweka Developments</div>
    </footer>
  </main>
</body>
</html>
```